Motivationsplakat
Sehr schönes Design und sehr angenehme Zusammenarbeit. Ging umgehend auf meine Wünsche ein. Immer wieder gerne! Vielen Dank!
Zielgruppe
Wir, der SC Wendorf aus der Schweiz, sind ein Fussballverein welcher in der 4. höchsten Liga spielt. Der hier zu erstellende Banner (Fusszeile) ist vorwiegend für die Spieler der 1. Mannschaft, als 'Motivationsspritze' auf diversen Plakaten (z.B. auf A1 Plakat wo die Aufstellung draufgeschrieben wird), gedacht.
Aufgabenstellung
Der Banner (als Fussleiste eines Plakates oder als eigenständiger Banner benutzbar) sollte ein Verhältniss von 1 zu 4 haben (also z.B. 50 cm hoch und 200 cm breit). Auf dem Banner muss das Logo des SC Wendorf drauf sein (im Anhang). Dazu muss es folgende Texte enthalten:
- Saison 2017/18
- Die Leidenschaft und den Verein im Herzen!
Der Spruch sollte als zentrale Botschaft verstanden werden und durch die grafische Gestalltung verstärkt/unterstützt werden.
Im Anhang sende ich ihnen noch ein paar Fotos von Spielern, welche sie eventuell verwenden könnten (muss nicht sein). Es dürften jedoch keine Spielergesichter erkennbar sein, also nur z.B. das Dress.

```html
<!DOCTYPE html>
<html lang="de">
<head>
<meta charset="utf-8">
<title>SC Wendorf – Saison 2017/18 Banner</title>
<link rel="stylesheet" href="https://fonts.googleapis.com/css2?family=Bebas+Neue&display=swap">
<style>
  :root {
    --bg-dark: #1c1306;
    --bg-mid: #4f3a10;
    --bg-gold: #7d5f18;
    --fire-red: #c85a10;
    --fire-orange: #e58a1c;
    --fire-yellow: #f7c040;
    --ball-light: #f0a94a;
    --ball-mid: #c97a28;
    --ball-dark: #6b3c12;
    --text-white: #ffffff;
  }
  html, body {
    margin: 0;
    padding: 0;
    width: 1200px;
    height: 300px;
    overflow: hidden;
    background: var(--bg-dark);
  }
  .banner {
    position: relative;
    width: 1200px;
    height: 300px;
    overflow: hidden;
    font-family: "Bebas Neue", "Arial Narrow", sans-serif;
    color: var(--text-white);
  }
  .banner__backdrop {
    position: absolute;
    inset: 0;
    background:
      radial-gradient(ellipse 260px 220px at 620px 150px, rgba(229,138,28,0.9) 0%, rgba(200,90,16,0.55) 45%, rgba(200,90,16,0) 100%),
      radial-gradient(ellipse 750px 320px at 480px 140px, var(--bg-gold) 0%, var(--bg-mid) 45%, var(--bg-dark) 100%);
  }
  .banner__fireball {
    position: absolute;
    left: 400px;
    top: 0;
    width: 440px;
    height: 300px;
  }
  .banner__headline {
    position: absolute;
    left: 35px;
    top: 20px;
    margin: 0;
    font-weight: 400;
    font-size: 64px;
    line-height: 65px;
    letter-spacing: 0.5px;
    white-space: nowrap;
  }
  .banner__season {
    position: absolute;
    left: 35px;
    top: 226px;
    margin: 0;
    font-size: 44px;
    line-height: 44px;
    letter-spacing: 0.5px;
    white-space: nowrap;
  }
  .banner__club {
    position: absolute;
    left: 858px;
    top: 112px;
    display: flex;
    align-items: center;
    gap: 14px;
    white-space: nowrap;
  }
  .banner__club-mark {
    width: 64px;
    height: 64px;
    border-radius: 50%;
    background: var(--text-white);
    flex: none;
  }
  .banner__club-name {
    font-size: 64px;
    line-height: 64px;
    letter-spacing: 1px;
    color: var(--text-white);
  }
</style>
</head>
<body>
  <div class="banner">
    <div class="banner__backdrop"></div>
    <svg class="banner__fireball" viewBox="0 0 440 300" role="img" aria-label="Brennender Fussball, von Flammen umgeben">
      <defs>
        <radialGradient id="flame-glow" cx="50%" cy="55%" r="50%">
          <stop offset="0%" stop-color="var(--fire-yellow)" stop-opacity="0.9"/>
          <stop offset="55%" stop-color="var(--fire-orange)" stop-opacity="0.7"/>
          <stop offset="100%" stop-color="var(--fire-red)" stop-opacity="0"/>
        </radialGradient>
        <radialGradient id="ball-shade" cx="42%" cy="38%" r="65%">
          <stop offset="0%" stop-color="var(--ball-light)"/>
          <stop offset="60%" stop-color="var(--ball-mid)"/>
          <stop offset="100%" stop-color="var(--ball-dark)"/>
        </radialGradient>
      </defs>
      <ellipse cx="220" cy="170" rx="220" ry="170" fill="url(#flame-glow)"/>
      <circle cx="220" cy="205" r="155" fill="url(#ball-shade)"/>
    </svg>
    <h1 class="banner__headline">Die Leidenschaft<br>und den<br>Verein im Herzen!</h1>
    <p class="banner__season">Saison 2017/18</p>
    <div class="banner__club">
      <span class="banner__club-mark"></span>
      <span class="banner__club-name">SC Wendorf</span>
    </div>
  </div>
</body>
</html>
```